Bright Vale Inc - Cutting-Edge Biotech Laboratory - Sleek & Sophisticated

Please design a website that has more of a high-tech and high-end feel, with contents outlined in the uploaded file.

Please have main tabs of the following categories: Home, About, FDA & LAWS, Science, Products, Media, Contact.

Media can include all the videos and photos.

Current website: www.brightvaleprime.com - it needs to be much more high-end, sleek and more organized. Please do NOT follow the outlines in the old website, but follow the uploaded CONTENT file.

Target Market(s)

doctors

Industry/Entity Type

Biotechnology

Coding

Coded - Design and coding required

Number of Pages Required

5+ page

Requirements
Must have
• Logo
Nice to have
• Some lotion on the website

```html
<!DOCTYPE html>
<html lang="en">
<head>
<meta charset="utf-8">
<title>Bright Vale Inc</title>
<link href="https://fonts.googleapis.com/css2?family=Open+Sans:wght@400;600;700&family=Montserrat:wght@500;600;700&display=swap" rel="stylesheet">
<style>
:root{
  --blue:#1c6fd1;
  --blue-dark:#0b1d3d;
  --navy:#14284b;
  --ink:#1d2433;
  --text:#6b7482;
  --muted:#9aa3b0;
  --line:#e3e7ee;
  --soft:#f4f6fa;
  --white:#ffffff;
}
*{box-sizing:border-box;margin:0;padding:0}
html,body{width:1200px;height:3240px;overflow:hidden}
body{font-family:"Open Sans",Arial,sans-serif;color:var(--text);background:var(--white);font-size:13px;line-height:1.6}
h1,h2,h3,h4{font-family:"Montserrat",Arial,sans-serif;color:var(--ink)}
.wrap{width:1040px;margin:0 auto;position:relative}

/* header */
.site-header{height:56px;background:var(--white);border-bottom:1px solid var(--line)}
.site-header .wrap{display:flex;align-items:center;justify-content:space-between;height:56px}
.brand{display:flex;align-items:center;gap:10px;font-family:"Montserrat",sans-serif;font-weight:700;font-size:18px;color:var(--blue);letter-spacing:.5px}
.brand-dot{width:22px;height:22px;border-radius:50%;background:var(--blue)}
.main-nav{display:flex;gap:30px}
.main-nav a{font-family:"Montserrat",sans-serif;font-size:11px;font-weight:600;color:var(--ink);text-decoration:none;letter-spacing:.6px}

/* hero */
.hero{height:274px;position:relative;overflow:hidden}
.hero-bg{position:absolute;inset:0;background:radial-gradient(circle at 70% 40%,#3a6fb0 0%,#15335f 35%,#0a1a36 75%)}
.hero .wrap{padding-top:58px}
.hero h1{color:var(--white);font-size:30px;line-height:1.22;font-weight:600;width:560px}
.hero p{color:#c9d6ea;font-size:14px;margin-top:14px;width:330px;line-height:1.4}
.btn-outline{display:inline-block;margin-top:18px;padding:7px 18px;border:1px solid var(--white);border-radius:20px;color:var(--white);font-size:11px;font-weight:600}

/* section heads */
.eyebrow{font-size:12px;color:var(--blue);border-bottom:1px solid var(--line);padding-bottom:6px;width:90px}
.section-title{font-size:30px;font-weight:600;margin-top:6px}
.center{text-align:center}
.center .eyebrow{margin:0 auto}

/* about */
.about{height:400px;padding-top:40px}
.about-text{width:540px}
.about-text p{margin-top:16px;font-size:12px}
.btn-row{display:flex;gap:14px;margin-top:26px}
.btn{padding:9px 26px;border-radius:22px;font-size:11px;font-weight:600}
.btn-primary{background:var(--blue);color:var(--white)}
.btn-ghost{border:1px solid var(--line);color:var(--blue)}
.about-photo{position:absolute;right:0;top:18px;width:380px;height:250px;background:linear-gradient(135deg,#e8edf3,#c9d3df 60%,#f3f5f8)}

/* services */
.services{height:740px;background:var(--soft);padding-top:40px}
.services-intro{width:380px;margin-top:14px;font-size:12px}
.services-body{display:flex;margin-top:36px;gap:40px}
.service-list{width:300px;list-style:none}
.service-list li{display:flex;align-items:center;gap:18px;height:80px;padding-left:16px;font-size:12px;color:var(--ink)}
.service-list li.active{background:var(--white);box-shadow:0 4px 16px rgba(20,40,75,.08)}
.service-icon{width:44px;height:44px;border-radius:50%;background:radial-gradient(circle,#6b7fb8,#1f2b5a)}
.service-detail{flex:1;padding-top:14px}
.service-detail h3{font-size:20px;font-weight:600}
.service-detail p{font-size:12px;margin-top:14px}
.details-link{display:block;color:var(--blue);font-size:12px;margin-top:14px;font-weight:600}
.service-gallery{display:flex;gap:18px;margin-top:22px}
.service-gallery div{flex:1;height:140px}
.g1{background:linear-gradient(135deg,#e9d6c9,#c79e8a)}
.g2{background:linear-gradient(135deg,#bfe3f5,#2f86c2)}
.g3{background:linear-gradient(135deg,#e7c7b3,#a56c58)}

/* testimonials */
.testimonials{height:640px;padding-top:40px}
.testimonials .lead{width:380px;margin:12px auto 0;font-size:12px}
.quote-grid{display:grid;grid-template-columns:1fr 1fr;margin-top:50px;position:relative}
.quote-grid::before{content:"";position:absolute;left:50%;top:0;bottom:0;border-left:1px solid var(--line)}
.quote-grid::after{content:"";position:absolute;top:50%;left:0;right:0;border-top:1px solid var(--line)}
.quote{display:flex;gap:20px;padding:40px 30px;align-items:flex-start}
.quote.left{flex-direction:row-reverse}
.quote p{font-size:12px}
.quote cite{display:block;font-style:normal;color:var(--ink);font-size:11px;margin-top:10px;font-weight:600}
.quote.left cite{text-align:right}
.avatar{flex:0 0 60px;height:60px;border-radius:50%;background:linear-gradient(135deg,#d8c3b3,#8a6a58)}

/* news */
.news{height:620px;background:var(--soft);padding-top:40px}
.news-intro{width:380px;margin-top:14px;font-size:12px}
.news-grid{display:grid;grid-template-columns:repeat(4,1fr);gap:20px;margin-top:34px}
.card{background:var(--white);box-shadow:0 3px 12px rgba(20,40,75,.06)}
.card-img{height:190px}
.n1{background:linear-gradient(160deg,#7a5a44,#2f2620)}
.n2{background:linear-gradient(160deg,#b06a3c,#4a2c1e)}
.n3{background:linear-gradient(160deg,#9d7c62,#3d3028)}
.n4{background:linear-gradient(160deg,#d7cfc6,#8d7b6d)}
.card-body{padding:16px 18px 14px}
.card h4{font-size:17px;font-weight:600}
.card p{font-size:11px;margin-top:8px}
.card-meta{display:flex;justify-content:space-between;border-top:1px solid var(--line);margin-top:14px;padding-top:10px;font-size:10px;color:var(--muted)}

/* footer info */
.footer-info{height:340px;padding-top:50px}
.footer-cols{display:flex;justify-content:space-between}
.footer-col h4{font-size:14px;font-weight:700;border-bottom:2px solid var(--blue);padding-bottom:8px;margin-bottom:16px}
.doctors{width:420px}
.doctors .grid{display:grid;grid-template-columns:1fr 1fr;row-gap:18px}
.chief{width:280px}
.chief .grid{display:grid;grid-template-columns:1fr 1fr}
.hq{width:240px}
.hq .grid{display:grid;grid-template-columns:1fr 1fr}
.contact{font-size:11px;line-height:1.55}
.contact strong{display:block;color:var(--ink);font-weight:600}

/* bottom bar */
.bottom-bar{height:170px;background:var(--soft);border-top:1px solid var(--line)}
.bottom-bar .wrap{display:flex;justify-content:space-between;padding-top:40px}
.foot-nav{display:flex;gap:26px;align-items:center}
.foot-nav a{font-family:"Montserrat",sans-serif;font-size:11px;font-weight:700;color:var(--ink);text-decoration:none}
.foot-nav .home-icon{width:14px;height:14px}
.sub-links{display:flex;gap:18px;margin-top:14px;font-size:10px;color:var(--muted)}
.foot-right{text-align:right}
.foot-right .legal{font-size:10px;color:var(--muted);margin-top:16px}
</style>
</head>
<body>

<header class="site-header">
  <div class="wrap">
    <div class="brand"><span class="brand-dot"></span>Bright Vale</div>
    <nav class="main-nav">
      <a href="#">ABOUT US</a><a href="#">FDA &amp; LAWS</a><a href="#">SCIENCE</a><a href="#">PRODUCTS</a><a href="#">MEDIA</a><a href="#">CONTACT US</a>
    </nav>
  </div>
</header>

<section class="hero">
  <div class="hero-bg" role="img" aria-label="Dark blue network of glowing connected points"></div>
  <div class="wrap">
    <h1>Leader in Regenerative Medicine<br>Innovator of the Industry<br>Never Compromises on Quality</h1>
    <p>Interview with Bright Vale chief scientist Marco Deltano on stem cells</p>
    <span class="btn-outline">Watch Interview</span>
  </div>
</section>

<section class="about">
  <div class="wrap">
    <div class="about-text">
      <div class="eyebrow">About Us</div>
      <h2 class="section-title">Who we are ?</h2>
      <p>Bright Vale Renewal Therapy provides Amniotic Stem Cells and unique protocols to doctors in order to help their patients who have lingering health conditions as well as individuals who simply wish to stay young and healthy.</p>
      <p>Over the past five years in development, we have successfully conducted research into targeted repair delivered straight to the source of the problem, and care trusted in helping people who have suffered stroke or brain injury to walk or talk again. We have become an industry leader in modern cell therapy and we have achieved significant results in fighting aging and its common markers.</p>
      <div class="btn-row"><span class="btn btn-primary">Contact Us</span><span class="btn btn-ghost">Read More</span></div>
    </div>
    <div class="about-photo" role="img" aria-label="Scientists in white lab coats working in a bright laboratory"></div>
  </div>
</section>

<section class="services">
  <div class="wrap">
    <div class="eyebrow">Services</div>
    <h2 class="section-title">What we do ?</h2>
    <p class="services-intro">Nam a perspiciatis unde omnis iste natus error sit voluptatem natione pariatur fugit sed quia consequuntur magni dolores.</p>
    <div class="services-body">
      <ul class="service-list">
        <li class="active"><span class="service-icon" role="img" aria-label="FDA and laws icon photo"></span>FDA &amp; LAWS</li>
        <li><span class="service-icon" role="img" aria-label="Transcription icon photo"></span>Transcription</li>
        <li><span class="service-icon" role="img" aria-label="Orthopedics icon photo"></span>Orthopedics</li>
        <li><span class="service-icon" role="img" aria-label="Hormone icon photo"></span>Hormone</li>
        <li><span class="service-icon" role="img" aria-label="Disease treatment icon photo"></span>Disease of good nations</li>
      </ul>
      <div class="service-detail">
        <h3>FDA &amp; LAWS</h3>
        <p>Sed ut perspiciatis unde omnis iste natus error sit voluptatem accusantium doloremque laudantium, totam rem aperiam, eaque ipsa quae ab illo inventore veritatis et quasi architecto beatae vitae dicta sunt explicabo. Nemo enim ipsam voluptatem quia voluptas sit aspernatur aut odit aut fugit, sed quia consequuntur magni dolores.</p>
        <p>Sed ut perspiciatis unde omnis iste natus error sit voluptatem accusantium doloremque laudantium, totam rem aperiam, eaque ipsa quae ab illo inventore veritatis et quasi architecto.</p>
        <span class="details-link">Details »</span>
        <div class="service-gallery">
          <div class="g1" role="img" aria-label="Close view of skin treatment"></div>
          <div class="g2" role="img" aria-label="Blue cell microscopy image"></div>
          <div class="g3" role="img" aria-label="Series of before and after treatment views"></div>
        </div>
      </div>
    </div>
  </div>
</section>

<section class="testimonials">
  <div class="wrap center">
    <div class="eyebrow">Testimonials</div>
    <h2 class="section-title">What Our Client Says ?</h2>
    <p class="lead">Vitae ut dignis ipsum ut laoreet amet feus est lectus, at oreet vitae sit amet auctor nibh.</p>
  </div>
  <div class="wrap">
    <div class="quote-grid">
      <div class="quote left"><span class="avatar" role="img" aria-label="Client portrait"></span><div><p>Duis aute irure dolor in reprehenderit in voluptate velit esse cillum dolore eu fugiat nulla pariatur. Excepteur sint occaecat cupidatat non proident, sunt in culpa qui officia deserunt mollit.</p><cite>Dan Carver, Operations Manager</cite></div></div>
      <div class="quote"><span class="avatar" role="img" aria-label="Client portrait"></span><div><p>Phasellus, tempus sed in quisque ad diam dapibus mollis enim, amet auctor. Aliquam erat volutpat, nam ut libero turpis quis dapibus efficitur, nam libero tempor, cum soluta nobis.</p><cite>Lena Grove, Creative Designer</cite></div></div>
      <div class="quote left"><span class="avatar" role="img" aria-label="Client portrait"></span><div><p>Duis aute irure dolor in reprehenderit in voluptate velit esse cillum dolore eu fugiat nulla pariatur. Excepteur sint occaecat cupidatat non proident, sunt in culpa qui officia deserunt mollit.</p><cite>Marta Lind, Manager</cite></div></div>
      <div class="quote"><span class="avatar" role="img" aria-label="Client portrait"></span><div><p>At vero eos et accusamus et iusto odio dignissimos ducimus qui blanditiis praesentium voluptatum deleniti atque corrupti quos dolores et quas molestias excepturi sint.</p><cite>Tim Larsen, Developer</cite></div></div>
    </div>
  </div>
</section>

<section class="news">
  <div class="wrap">
    <div class="eyebrow">Media</div>
    <h2 class="section-title">Latest News &amp; Views</h2>
    <p class="news-intro">Natus porro adipisci nisi. Ut tempor kasd ipsum dolor sit amet, consetetur, elitrm nibh, sed tum no.</p>
    <div class="news-grid">
      <article class="card"><div class="card-img n1" role="img" aria-label="Wooden interior with chair"></div><div class="card-body"><h4>Standard Post</h4><p>Enim congue blandit lorem ipsum dolor sit amet, consetetur sadipscing elitr.</p><div class="card-meta"><span>22 June, 2015</span><span>5</span></div></div></article>
      <article class="card"><div class="card-img n2" role="img" aria-label="Warm lit room with furniture"></div><div class="card-body"><h4>Video Post</h4><p>Ultrices posuere cubilia curae pretium sit amet dolor, a massa pulvinar lorem.</p><div class="card-meta"><span>22 June, 2015</span><span>5</span></div></div></article>
      <article class="card"><div class="card-img n3" role="img" aria-label="Brick wall with rustic shelving"></div><div class="card-body"><h4>Post with Image</h4><p>Enim congue blandit lorem ipsum dolor sit amet, consetetur sadipscing elitr.</p><div class="card-meta"><span>22 June, 2015</span><span>5</span></div></div></article>
      <article class="card"><div class="card-img n4" role="img" aria-label="Light interior with decorative objects"></div><div class="card-body"><h4>Image Post</h4><p>Ultrices posuere cubilia curae pretium sit amet dolor, a massa pulvinar lorem.</p><div class="card-meta"><span>22 June, 2015</span><span>5</span></div></div></article>
    </div>
  </div>
</section>

<section class="footer-info">
  <div class="wrap footer-cols">
    <div class="footer-col doctors">
      <h4>Doctors Offices</h4>
      <div class="grid">
        <div class="contact"><strong>Dr. Owen P. Hartley</strong>Vale Center for Cell Renewal<br>Harrow Bay, ST 00412</div>
        <div class="contact"><strong>Dr. Lucas Brennholt</strong>Birchline Clinic, Suite 2C<br>Lindmoor, ST 00587</div>
        <div class="contact"><strong>Dr. Adrian Selby</strong>36 Quarry Hill Lane, Unit 5<br>Quillfield, ST 00731</div>
        <div class="contact"><strong>Dr. Gregory M. Tallis</strong>Fernway Health, 9 Ridge Court<br>Ashcombe, ST 00265</div>
      </div>
    </div>
    <div class="footer-col chief">
      <h4>Chief</h4>
      <div class="grid">
        <div class="contact"><strong>Marco Deltano</strong>Chief Scientist<br>+1 (555) 014-8200</div>
        <div class="contact"><strong>Elena Marsh</strong>Stem Cell Manager<br>+1 (555) 014-8311</div>
      </div>
    </div>
    <div class="footer-col hq">
      <h4>Headquarters</h4>
      <div class="grid">
        <div class="contact"><strong>Main Office</strong>4560 Vale Street<br>Suite 120<br>Harrow Bay, ST 00410</div>
        <div class="contact"><strong>Email</strong>info@brightvaleprime.com</div>
      </div>
    </div>
  </div>
</section>

<footer class="bottom-bar">
  <div class="wrap">
    <div>
      <nav class="foot-nav">
        <svg class="home-icon" viewBox="0 0 14 14"><path d="M1 7 7 1l6 6M3 6v7h8V6" fill="none" stroke="#1d2433" stroke-width="1.6"/></svg>
        <a href="#">HELP &amp; CONTACT</a><a href="#">FDA &amp; LAWS</a><a href="#">SCIENCE</a><a href="#">PRODUCTS</a>
      </nav>
      <div class="sub-links"><span>About</span><span>Media</span><span>Careers</span><span>Privacy Policy</span><span>Sitemap</span><span>Science</span><span>Products</span></div>
    </div>
    <div class="foot-right">
      <div class="brand"><span class="brand-dot"></span>Bright Vale</div>
      <div class="legal">© 2015 Bright Vale Inc &nbsp; Privacy &nbsp; Legal &nbsp; Feedback</div>
    </div>
  </div>
</footer>

</body>
</html>
```